Direct Mail Postcard for new client solicitation

I need a postcard designed to market our full service accounting and financial services firm to local companies.

Our firm specializes in outsourced accounting and finance - we do everything from book keeping all the way up to financial oversight. We prefer to work on a flat fee recurring revenue basis rather than a traditional hourly fee. We also bring our own privately developed software to assist with the process. This software is proprietary in nature and not available elsewhere.

This card should convey:
1. Transferring financial headaches to a qualified company.
2. Stable access to help.
3. Cost savings.
4. A comprehensive package that allows for the client to take as much or as little as they would like.

I have attached our logo as a starting point. Feel free to engage us with questions and for guidance.

The company name is BrightLedgerPro.

Target Market(s)

the target market for this project is small businesses in the chicago area (our test market) with annual revenues between 5 and 10 Million dollars

Industry/Entity Type

Accounting

Font styles to use
Serif
Sans Serif

Requirements
Must have
• The project must convey the idea that we are taking administrative burdens and headaches from the client. The idea is that they are outsourcing their back office accounting functions to us while still retaining overall control of the process. The card must convey this concept somehow.
• We are also working on copy - since we are accountants and basically as boring as watching paint dry we are struggling a bit. Feel free to take a stab at copy as well. Keep in mind - we do not need to say alot - ideally we would say in essence "outsource your finance and accounting work to us for a reasonable fixed price".
Should not have
• We are reworking our website as well. The little orange guys and in fact the entire copy will be changing over the next few weeks. We would prefer to avoid using that motif for the card.

```html
<!DOCTYPE html>
<html lang="en">
<head>
<meta charset="utf-8">
<title>BrightLedgerPro Postcard</title>
<link rel="stylesheet" href="https://fonts.googleapis.com/css2?family=Source+Sans+3:wght@400;600;700;800&display=swap">
<style>
  :root {
    --stage: #5a5a5a;
    --paper: #ffffff;
    --teal: #5fd0e2;
    --sky: #1b92dc;
    --navy: #1020b0;
    --ink: #111111;
    --pill-top: #4d8cf0;
    --pill-bottom: #1638c8;
  }
  * { margin: 0; padding: 0; box-sizing: border-box; }
  html, body { width: 900px; height: 1200px; overflow: hidden; }
  body {
    position: relative;
    background: var(--stage);
    font-family: "Source Sans 3", "Segoe UI", sans-serif;
  }
  .card {
    position: absolute;
    left: 26px;
    width: 850px;
    height: 546px;
    background: var(--paper);
    overflow: hidden;
  }
  .card--front { top: 38px; }
  .card--back { top: 616px; }
  .card__art { position: absolute; inset: 0; }

  .brand {
    position: absolute;
    display: flex;
    align-items: center;
    gap: 8px;
    font-weight: 800;
    color: var(--ink);
    letter-spacing: -0.5px;
    white-space: nowrap;
  }
  .brand__square { display: inline-block; background: var(--sky); }
  .card--front .brand { left: 36px; top: 22px; font-size: 30px; }
  .card--front .brand__square { width: 22px; height: 22px; }

  .headline {
    position: absolute;
    right: 24px;
    top: 22px;
    text-align: right;
    color: #fff;
    font-weight: 700;
    font-size: 25px;
    line-height: 31px;
  }
  .intro {
    position: absolute;
    left: 352px;
    top: 156px;
    width: 392px;
    color: var(--sky);
    font-size: 12.6px;
    line-height: 19.4px;
  }
  .help-pill {
    position: absolute;
    left: 491px;
    top: 312px;
    width: 169px;
    height: 28px;
    border-radius: 9px;
    background: linear-gradient(var(--pill-top), var(--pill-bottom));
    color: #fff;
    font-weight: 700;
    font-size: 18px;
    line-height: 28px;
    text-align: center;
  }
  .services {
    position: absolute;
    list-style: none;
    color: var(--sky);
    font-size: 15px;
    line-height: 19.4px;
  }
  .services li { position: relative; padding-left: 12px; }
  .services li::before {
    content: "";
    position: absolute;
    left: 0;
    top: 7px;
    width: 6px;
    height: 6px;
    border-radius: 50%;
    background: var(--navy);
  }
  .services--left { left: 404px; top: 356px; }
  .services--right { left: 610px; top: 365px; }
  .tagline {
    position: absolute;
    left: 359px;
    top: 488px;
    color: var(--navy);
    font-weight: 700;
    font-size: 21px;
    white-space: nowrap;
  }

  .card--back .brand { left: 82px; top: 230px; font-size: 47px; gap: 12px; }
  .card--back .brand__square { width: 34px; height: 34px; }
  .website {
    position: absolute;
    left: 160px;
    top: 490px;
    color: var(--sky);
    font-size: 19px;
  }
  .divider {
    position: absolute;
    left: 496px;
    top: 86px;
    width: 3px;
    height: 366px;
    background: var(--ink);
  }
  .stamp-box {
    position: absolute;
    left: 686px;
    top: 100px;
    width: 71px;
    height: 91px;
    border: 1.5px dashed #333;
  }
  .address-line {
    position: absolute;
    left: 552px;
    width: 210px;
    height: 2.5px;
    background: var(--ink);
  }
</style>
</head>
<body>

<section class="card card--front">
  <svg class="card__art" width="850" height="546" viewBox="0 0 850 546">
    <defs>
      <linearGradient id="topWash" x1="0" y1="0" x2="1" y2="0.3">
        <stop offset="0" stop-color="#f4fbfd"/>
        <stop offset="1" stop-color="#58cde0"/>
      </linearGradient>
      <linearGradient id="photoTone" x1="0" y1="0" x2="1" y2="1">
        <stop offset="0" stop-color="#d9cfc2"/>
        <stop offset="0.45" stop-color="#eee9e0"/>
        <stop offset="0.75" stop-color="#b7a6b8"/>
        <stop offset="1" stop-color="#5d6f95"/>
      </linearGradient>
    </defs>
    <rect width="850" height="546" fill="url(#topWash)"/>
    <path d="M0,546 L0,145 C160,85 360,70 520,115 C650,155 770,215 850,240 L850,546 Z" fill="#fff"/>
    <circle cx="160" cy="326" r="178" fill="var(--navy)"/>
    <circle cx="168" cy="296" r="178" fill="#fff"/>
    <circle cx="168" cy="294" r="172" fill="url(#photoTone)" role="img" aria-label="Photo of a hand writing service notes in a notebook beside a calculator and coffee cup"/>
  </svg>

  <div class="brand"><span>BrightLedgerPro</span><span class="brand__square"></span></div>

  <h1 class="headline">Finally - a way to outsource those<br>financial headaches without<br>losing control!</h1>

  <p class="intro">BrightLedgerPro is more than a consulting firm –<br>we are a partner that provides a total solution for all your financial headaches. BrightLedgerPro is a revolutionary way to handle your business finances. Using proprietary tools that allow you to control and monitor the processing of data we provide the most comprehensive solution to all your accounting and finance issues! Now you can move just the issues you want - at prices you can afford</p>

  <div class="help-pill">We can help with</div>

  <ul class="services services--left">
    <li>Financial management</li>
    <li>Accounting</li>
    <li>Book keeping</li>
    <li>Forecasting</li>
    <li>Reporting</li>
  </ul>
  <ul class="services services--right">
    <li>Bank management</li>
    <li>Fund raising</li>
    <li>Business transition planning</li>
    <li>Tax compliance</li>
  </ul>

  <p class="tagline">If you have headaches we have solutions!</p>
</section>

<section class="card card--back">
  <svg class="card__art" width="850" height="546" viewBox="0 0 850 546">
    <defs>
      <linearGradient id="cornerTop" x1="0" y1="1" x2="1" y2="0">
        <stop offset="0" stop-color="#4cc6dc"/>
        <stop offset="1" stop-color="#ffffff"/>
      </linearGradient>
      <linearGradient id="cornerBottom" x1="0" y1="0" x2="1" y2="1">
        <stop offset="0" stop-color="#ffffff"/>
        <stop offset="1" stop-color="#45c2da"/>
      </linearGradient>
    </defs>
    <path d="M0,0 H380 C230,35 80,110 0,200 Z" fill="url(#cornerTop)"/>
    <path d="M850,546 V355 C780,430 650,505 500,546 Z" fill="url(#cornerBottom)"/>
  </svg>

  <div class="brand"><span>BrightLedgerPro</span><span class="brand__square"></span></div>
  <p class="website">www.brightledgerpro.com</p>

  <div class="divider"></div>
  <div class="stamp-box"></div>
  <div class="address-line" style="top:241px"></div>
  <div class="address-line" style="top:291px"></div>
  <div class="address-line" style="top:337px"></div>
  <div class="address-line" style="top:384px"></div>
</section>

</body>
</html>
```